Stationery for new photography studio
Flyer, Gift Certificate, Business Card, headed paper, CD label and case cover
Please note the change in email address
studio@brightferndesigns.at
Dear sir,
Thanks for your feedback.
#100 is brilliant
I really like #97. I love the colours from the photos. I like the new business cards. Could you combine the concepts in the business cards from #94 #96 #97
temp web address
http://brightferndesigns.snapvault-host.com/
#89 every thing looks great. A few comments:
1) The business cards - I like the logo side however the information side I prefer earlier designs where you used one block colour ie- #87 or #49. I'm still not sure about this side.
2) The dark black logo square on the paper looks too bold.
Great work. Thanks a lot.
Please check the newly uploaded files.
PANTONES:
Blue: 310 C
Brown: 409 C
Pink: 211 C
Gray: 424 C
FONTS:
Petra: Gotham Medium
Valkenor: Gotham Book
Tagline: Gotham Book
Signature: Custom made
I think I prefer the logo in #52 where it is slightly off the page than #70 where it is completely visible.
I like #70, it's sophisticated however the colour scheme is starting depart from the original and from the style of my work, which I think is not so heavy.
If you have any change or better suggestions please let me know.
Thank you.
#61 - #64 I'm not sure if the dots down the sides are necessary.
My website is down. But I'LL let you know when it's back up so you can take a look at some more pictures. I love the use of them in your designs. So excited by what I'm seeing. Thanks for your work so far.
#57. I love it. Everything adds up perfectly. Not sure about the font. It's a bit clumsy. I'd like something sharper and sleeker.
Great direction.
Does this work for A6
A CD disk is 120 mm in diameter (60 mm radius), with a hole 15 mm diameter (7.5 mm radius)
I'm looking on google for CD dimensions. So far I've found the case cover dimensions:
CD Cover Size Specifications for Printing
The finished dimensions for the outside of printed CD covers are 4.724 inches square. Many printed designs include bleed. The "bleed area" is an extra 1/8" of space for design elements or backgrounds to extend beyond the finished size of your piece. A CD cover with bleeds is printed slightly oversized (4.974 inches square) and then cut down to size, giving the appearance that the printing "bleeds" off the edge of the cover rather than having a white border.
Really like the direction of #51 and #52. Re. #55 I prefer the designs where all embellishments or lines are relevant. What I mean by this is that the curve does not tie in anywhere. It's an additional form that is not part of the logo.
#61 and #62 are great. Can you show me some alternative fonts for the 15% and the brightferndesigns.at
This is fun project! What size should be the CD label be? I am not too sure!
#36 with black background?
I'd be interested to see #34 with black replacing the pink.
I have uploaded information to be included in the flyers and gift certificate.
Please look at my photos to understand my style
http://www.facebook.com/BrightFern.Designs?sk=app_274930158846320

```html
<!DOCTYPE html>
<html lang="en">
<head>
<meta charset="utf-8">
<title>Gift Certificate – Photographic Session</title>
<link href="https://fonts.googleapis.com/css2?family=Montserrat:wght@300;400;500;700&family=Dancing+Script:wght@400&display=swap" rel="stylesheet">
<style>
  :root {
    --ink: #000000;
    --paper: #ffffff;
    --pink: #f0a2c8;
    --pink-deep: #e48bb8;
    --skin-light: #e9c9b4;
    --skin-mid: #c99a82;
    --shade: #3a2a24;
    --blanket: #d9d6d4;
  }
  html, body {
    margin: 0;
    padding: 0;
    width: 1200px;
    height: 778px;
    overflow: hidden;
    background: var(--ink);
  }
  .certificate {
    position: relative;
    width: 1200px;
    height: 778px;
    background: var(--ink);
    overflow: hidden;
    font-family: "Montserrat", sans-serif;
    color: var(--paper);
  }
  .photo-area {
    position: absolute;
    top: 0;
    right: 0;
    width: 760px;
    height: 778px;
    background:
      radial-gradient(ellipse 300px 320px at 440px 300px, var(--skin-light) 0%, var(--skin-mid) 55%, rgba(201,154,130,0) 100%),
      radial-gradient(ellipse 520px 300px at 520px 700px, var(--blanket) 0%, rgba(217,214,212,0) 100%),
      linear-gradient(180deg, #5a4a44 0%, var(--shade) 50%, #6d625e 100%);
  }
  .photo-fade {
    position: absolute;
    top: 0;
    left: 0;
    width: 760px;
    height: 778px;
    background: linear-gradient(90deg, var(--ink) 0%, rgba(0,0,0,0.85) 25%, rgba(0,0,0,0) 60%);
  }
  .brand {
    position: absolute;
    left: 96px;
    top: 40px;
    width: 400px;
    text-align: center;
  }
  .brand-mark {
    display: block;
    margin: 0 auto 10px;
  }
  .brand-name {
    font-size: 38px;
    letter-spacing: 5px;
    line-height: 1;
    white-space: nowrap;
  }
  .brand-name .first { font-weight: 500; }
  .brand-name .last { font-weight: 300; }
  .brand-tagline {
    margin-top: 8px;
    font-size: 13px;
    font-weight: 400;
    letter-spacing: 4px;
    color: var(--pink);
  }
  .offer {
    position: absolute;
    left: 40px;
    top: 228px;
    width: 520px;
    text-align: center;
  }
  .offer-title {
    font-size: 40px;
    font-weight: 700;
    line-height: 1;
  }
  .offer-session {
    margin-top: 10px;
    font-family: "Dancing Script", cursive;
    font-size: 60px;
    color: var(--pink);
    line-height: 1;
  }
  .offer-duration {
    margin-top: 14px;
    font-size: 58px;
    font-weight: 700;
    line-height: 1;
  }
  .field {
    position: absolute;
    left: 96px;
    display: flex;
    align-items: flex-end;
    font-family: "Dancing Script", cursive;
    font-size: 32px;
    color: var(--paper);
  }
  .field-line {
    height: 2px;
    background: var(--paper);
    margin-left: 6px;
    margin-bottom: 6px;
  }
  .field-to { top: 470px; }
  .field-to .field-line { width: 400px; }
  .field-from { top: 576px; }
  .field-from .field-line { width: 316px; margin-left: 14px; }
  .website {
    position: absolute;
    left: 96px;
    top: 652px;
    font-size: 38px;
    font-weight: 500;
    color: var(--pink);
  }
</style>
</head>
<body>
  <div class="certificate">
    <div class="photo-area" role="img" aria-label="Soft-lit photograph of a baby lying on a pale blanket, looking toward the viewer"></div>
    <div class="photo-fade"></div>

    <div class="brand">
      <svg class="brand-mark" width="60" height="60" viewBox="0 0 60 60" aria-hidden="true">
        <circle cx="30" cy="30" r="24" fill="none" stroke="var(--pink)" stroke-width="5"/>
      </svg>
      <div class="brand-name"><span class="first">Petra</span> <span class="last">Valkenor</span></div>
      <div class="brand-tagline">BRIGHT FERN DESIGNS</div>
    </div>

    <div class="offer">
      <div class="offer-title">Gift Certificate</div>
      <div class="offer-session">Photographic Session</div>
      <div class="offer-duration">1 hour</div>
    </div>

    <div class="field field-to"><span>To</span><span class="field-line"></span></div>
    <div class="field field-from"><span>From</span><span class="field-line"></span></div>

    <div class="website">Brightferndesigns.at</div>
  </div>
</body>
</html>
```